Dog treat bakery needs updated bag labels

We're a small-batch dog treat bakery and would like to update our front bag labels to 1) differentiate our line of products and 2) to stand out on shelves. We believe all dogs deserve to eat clean, healthy foods. That's why we bake low-calorie, clean treats made with simple, premium ingredients like teff, amaranth, and sorghum flours and 100% blueberry, carrot, and purple sweet potato. All our treats are made gluten free without preservatives, artificial flavors, soy, corn, wheat, or eggs. Clean treats, happy dogs!

see uploaded files

```html
<!DOCTYPE html>
<html lang="en">
<head>
<meta charset="utf-8">
<title>Goofy Pup – Treat Bag Labels</title>
<link rel="stylesheet" href="https://fonts.googleapis.com/css2?family=Oswald:wght@400&family=Arvo:wght@700&display=swap">
<style>
  :root {
    --teal: #1b9ca4;
    --teal-soft: #2aaab1;
    --white: #ffffff;
    --brown: #8c3b1c;
    --charcoal: #333333;
    --blueberry: #2d5ea8;
    --carrot: #f07522;
    --peanut: #c99779;
    --grape: #ad79bd;
  }
  * { box-sizing: border-box; margin: 0; padding: 0; }
  html, body { width: 686px; height: 1200px; overflow: hidden; background: var(--white); }
  .sheet { position: relative; width: 686px; height: 1200px; }

  .label {
    position: absolute; width: 283px; height: 164px;
    background: var(--teal); overflow: hidden;
    font-family: "Oswald", "Arial Narrow", sans-serif; color: var(--white);
  }
  .label.col-a { left: 33px; --title-ink: var(--teal); }
  .label.col-b { left: 382px; --title-ink: var(--white); }
  .label.charcoal { --accent: var(--charcoal); }
  .label.blueberry { --accent: var(--blueberry); }
  .label.carrot { --accent: var(--carrot); }
  .label.peanut { --accent: var(--peanut); }
  .label.grape { --accent: var(--grape); }

  .hearts-pattern {
    position: absolute; left: 7px; top: 14px; width: 74px; height: 138px;
    background: var(--teal-soft); border-radius: 8px;
  }

  .front-panel { position: absolute; left: 76px; top: 0; width: 124px; height: 164px; }
  .front-panel svg { position: absolute; inset: 0; }
  .front-panel path { fill: var(--accent); }

  .kicker, .product-name, .seal-name { font-family: "Arvo", Georgia, serif; font-weight: 700; }
  .kicker {
    position: absolute; top: 8px; width: 100%; text-align: center;
    font-size: 5.6px; color: var(--title-ink); letter-spacing: 0.2px;
  }
  .category {
    position: absolute; top: 15px; width: 100%; text-align: center;
    font-size: 15px; line-height: 20px; letter-spacing: 0.3px;
  }
  .seal {
    position: absolute; left: 16px; top: 39px; width: 92px; height: 92px;
    border-radius: 50%; background: var(--white);
    display: flex; align-items: center; justify-content: center;
  }
  .seal-name { font-size: 13px; color: var(--brown); }
  .product-name {
    position: absolute; top: 137px; width: 100%; text-align: center; white-space: nowrap;
    font-size: 9.2px; line-height: 11px; color: var(--title-ink); letter-spacing: 0.5px;
  }
  .product-name .sub { display: block; font-size: 7.2px; line-height: 8px; }
  .net-weight {
    position: absolute; top: 151px; width: 100%; text-align: center;
    font-size: 4.8px; font-family: Georgia, serif;
  }
  .peanut .product-name { top: 134px; }
  .peanut .net-weight { top: 155px; }

  .claims {
    position: absolute; left: 213px; top: 17px; width: 68px;
    font-size: 8.2px; line-height: 11.8px; text-transform: uppercase;
  }
  .claims p + p { margin-top: 13px; }
  .claims.short { top: 31px; }
  .bone { display: inline-block; width: 14px; height: 8px; vertical-align: -1px; margin-left: 3px; }
  .bone path { fill: none; stroke: var(--white); stroke-width: 1; }

  .calorie-badge {
    position: absolute; left: 200px; top: 138px; width: 67px; height: 16px;
    border-radius: 8px; background: var(--accent); white-space: nowrap;
    font-size: 7.6px; line-height: 16px; text-align: center; text-transform: uppercase;
  }
  .calorie-badge.small { font-size: 5.6px; }
  .calorie-badge.tiny { left: 205px; font-size: 5.1px; }
</style>
</head>
<body>
<div class="sheet">

  <section class="label charcoal col-a" style="top:35px">
    <div class="hearts-pattern" role="img" aria-label="White outline hearts pattern"></div>
    <div class="front-panel">
      <svg viewBox="0 0 124 164"><path d="M16,0H108L116,55Q125,62 124,82Q125,102 116,110L108,164H16L8,110Q-1,102 0,82Q-1,62 8,55Z"/></svg>
      <div class="kicker">Limited Ingredient</div>
      <div class="category">DOG TREATS</div>
      <div class="seal"><span class="seal-name">Goofy Pup</span></div>
      <div class="product-name">Rosie’s Bites</div>
      <div class="net-weight">Net Wt 4 OZ (113g)</div>
    </div>
    <div class="claims"><p>No<br>Soy, corn,<br>wheat, eggs<br>or dairy</p><p>Made with<br>ancient grains<br>and grass fed<br>beef liver</p></div>
    <div class="calorie-badge">10 calories each</div>
  </section>
  <section class="label charcoal col-b" style="top:35px">
    <div class="hearts-pattern" role="img" aria-label="White outline hearts pattern"></div>
    <div class="front-panel">
      <svg viewBox="0 0 124 164"><path d="M16,0H108L116,55Q125,62 124,82Q125,102 116,110L108,164H16L8,110Q-1,102 0,82Q-1,62 8,55Z"/></svg>
      <div class="kicker">Limited Ingredient</div>
      <div class="category">DOG TREATS</div>
      <div class="seal"><span class="seal-name">Goofy Pup</span></div>
      <div class="product-name">Rosie’s Bites</div>
      <div class="net-weight">Net Wt 4 OZ (113g)</div>
    </div>
    <div class="claims"><p>No<br>Soy, corn,<br>wheat, eggs<br>or dairy</p><p>Made with<br>ancient grains<br>and grass fed<br>beef liver</p></div>
    <div class="calorie-badge">10 calories each</div>
  </section>

  <section class="label blueberry col-a" style="top:225px">
    <div class="hearts-pattern" role="img" aria-label="White outline hearts pattern"></div>
    <div class="front-panel">
      <svg viewBox="0 0 124 164"><path d="M16,0H108L116,55Q125,62 124,82Q125,102 116,110L108,164H16L8,110Q-1,102 0,82Q-1,62 8,55Z"/></svg>
      <div class="kicker">Limited Ingredient</div>
      <div class="category">DOG TREATS</div>
      <div class="seal"><span class="seal-name">Goofy Pup</span></div>
      <div class="product-name">Blueberry Burst</div>
      <div class="net-weight">Net Wt 4 OZ (113g)</div>
    </div>
    <div class="claims"><p>No<br>Soy, corn,<br>wheat, eggs<br>or dairy</p><p>100%<br>blueberry</p><p>Full of<br>antioxidants!</p></div>
    <div class="calorie-badge small">Only 1 calories each</div>
  </section>
  <section class="label blueberry col-b" style="top:225px">
    <div class="hearts-pattern" role="img" aria-label="White outline hearts pattern"></div>
    <div class="front-panel">
      <svg viewBox="0 0 124 164"><path d="M16,0H108L116,55Q125,62 124,82Q125,102 116,110L108,164H16L8,110Q-1,102 0,82Q-1,62 8,55Z"/></svg>
      <div class="kicker">Limited Ingredient</div>
      <div class="category">DOG TREATS</div>
      <div class="seal"><span class="seal-name">Goofy Pup</span></div>
      <div class="product-name">Blueberry Burst</div>
      <div class="net-weight">Net Wt 4 OZ (113g)</div>
    </div>
    <div class="claims"><p>No<br>Soy, corn,<br>wheat, eggs<br>or dairy</p><p>100%<br>blueberry</p><p>Full of<br>antioxidants!</p></div>
    <div class="calorie-badge small">Only 1 calories each</div>
  </section>

  <section class="label carrot col-a" style="top:418px">
    <div class="hearts-pattern" role="img" aria-label="White outline hearts pattern"></div>
    <div class="front-panel">
      <svg viewBox="0 0 124 164"><path d="M16,0H108L116,55Q125,62 124,82Q125,102 116,110L108,164H16L8,110Q-1,102 0,82Q-1,62 8,55Z"/></svg>
      <div class="kicker">Limited Ingredient</div>
      <div class="category">DOG TREATS</div>
      <div class="seal"><span class="seal-name">Goofy Pup</span></div>
      <div class="product-name">Comet Carrot</div>
      <div class="net-weight">Net Wt 4 OZ (113g)</div>
    </div>
    <div class="claims"><p>No<br>Soy, corn,<br>wheat, eggs<br>or dairy</p><p>Made with<br>carrot<br>and purple<br>sweet potato</p></div>
    <div class="calorie-badge">1.5 calories each</div>
  </section>
  <section class="label carrot col-b" style="top:418px">
    <div class="hearts-pattern" role="img" aria-label="White outline hearts pattern"></div>
    <div class="front-panel">
      <svg viewBox="0 0 124 164"><path d="M16,0H108L116,55Q125,62 124,82Q125,102 116,110L108,164H16L8,110Q-1,102 0,82Q-1,62 8,55Z"/></svg>
      <div class="kicker">Limited Ingredient</div>
      <div class="category">DOG TREATS</div>
      <div class="seal"><span class="seal-name">Goofy Pup</span></div>
      <div class="product-name">Comet Carrot</div>
      <div class="net-weight">Net Wt 4 OZ (113g)</div>
    </div>
    <div class="claims"><p>No<br>Soy, corn,<br>wheat, eggs<br>or dairy</p><p>Made with<br>carrot<br>and purple<br>sweet potato</p></div>
    <div class="calorie-badge">1.5 calories each</div>
  </section>

  <section class="label peanut col-a" style="top:613px">
    <div class="hearts-pattern" role="img" aria-label="White outline hearts pattern"></div>
    <div class="front-panel">
      <svg viewBox="0 0 124 164"><path d="M16,0H108L116,55Q125,62 124,82Q125,102 116,110L108,164H16L8,110Q-1,102 0,82Q-1,62 8,55Z"/></svg>
      <div class="kicker">Limited Ingredient</div>
      <div class="category">DOG TREATS</div>
      <div class="seal"><span class="seal-name">Goofy Pup</span></div>
      <div class="product-name">Peanut Butter<span class="sub">Yum Yums</span></div>
      <div class="net-weight">Net Wt 4 OZ (113g)</div>
    </div>
    <div class="claims"><p>No<br>Soy, corn, wheat,<br>eggs or dairy</p><p>Made with<br>real peanut<br>butter</p><p>Find <svg class="bone" viewBox="0 0 14 8"><path d="M3,6L11,2M1.5,5a1.3,1.3 0 1 0 2,2M2.5,4.5a1.3,1.3 0 1 0 1.5,2.5M12.5,3a1.3,1.3 0 1 0-2-2M11.5,3.5a1.3,1.3 0 1 0-1.5-2.5"/></svg><br>the lucky bone!</p></div>
    <div class="calorie-badge">3 calories each</div>
  </section>
  <section class="label peanut col-b" style="top:613px">
    <div class="hearts-pattern" role="img" aria-label="White outline hearts pattern"></div>
    <div class="front-panel">
      <svg viewBox="0 0 124 164"><path d="M16,0H108L116,55Q125,62 124,82Q125,102 116,110L108,164H16L8,110Q-1,102 0,82Q-1,62 8,55Z"/></svg>
      <div class="kicker">Limited Ingredient</div>
      <div class="category">DOG TREATS</div>
      <div class="seal"><span class="seal-name">Goofy Pup</span></div>
      <div class="product-name">Peanut Butter<span class="sub">Yum Yums</span></div>
      <div class="net-weight">Net Wt 4 OZ (113g)</div>
    </div>
    <div class="claims"><p>No<br>Soy, corn, wheat,<br>eggs or dairy</p><p>Made with<br>real peanut<br>butter</p><p>Find <svg class="bone" viewBox="0 0 14 8"><path d="M3,6L11,2M1.5,5a1.3,1.3 0 1 0 2,2M2.5,4.5a1.3,1.3 0 1 0 1.5,2.5M12.5,3a1.3,1.3 0 1 0-2-2M11.5,3.5a1.3,1.3 0 1 0-1.5-2.5"/></svg><br>the lucky bone!</p></div>
    <div class="calorie-badge">3 calories each</div>
  </section>

  <section class="label peanut col-a" style="top:806px">
    <div class="hearts-pattern" role="img" aria-label="White outline hearts pattern"></div>
    <div class="front-panel">
      <svg viewBox="0 0 124 164"><path d="M16,0H108L116,55Q125,62 124,82Q125,102 116,110L108,164H16L8,110Q-1,102 0,82Q-1,62 8,55Z"/></svg>
      <div class="kicker">Limited Ingredient</div>
      <div class="category">DOG TREATS</div>
      <div class="seal"><span class="seal-name">Goofy Pup</span></div>
      <div class="product-name">Peanut Butter<span class="sub">Yum Yums</span></div>
      <div class="net-weight">Net Wt 4 OZ (113g)</div>
    </div>
    <div class="claims"><p>No<br>Soy, corn, wheat,<br>eggs or dairy</p><p>Made with<br>real peanut<br>butter</p><p>Find <svg class="bone" viewBox="0 0 14 8"><path d="M3,6L11,2M1.5,5a1.3,1.3 0 1 0 2,2M2.5,4.5a1.3,1.3 0 1 0 1.5,2.5M12.5,3a1.3,1.3 0 1 0-2-2M11.5,3.5a1.3,1.3 0 1 0-1.5-2.5"/></svg><br>the lucky bone !</p></div>
    <div class="calorie-badge tiny">Less than 1 calories each</div>
  </section>
  <section class="label peanut col-b" style="top:806px">
    <div class="hearts-pattern" role="img" aria-label="White outline hearts pattern"></div>
    <div class="front-panel">
      <svg viewBox="0 0 124 164"><path d="M16,0H108L116,55Q125,62 124,82Q125,102 116,110L108,164H16L8,110Q-1,102 0,82Q-1,62 8,55Z"/></svg>
      <div class="kicker">Limited Ingredient</div>
      <div class="category">DOG TREATS</div>
      <div class="seal"><span class="seal-name">Goofy Pup</span></div>
      <div class="product-name">Peanut Butter<span class="sub">Yum Yums</span></div>
      <div class="net-weight">Net Wt 4 OZ (113g)</div>
    </div>
    <div class="claims"><p>No<br>Soy, corn, wheat,<br>eggs or dairy</p><p>Made with<br>real peanut<br>butter</p><p>Find <svg class="bone" viewBox="0 0 14 8"><path d="M3,6L11,2M1.5,5a1.3,1.3 0 1 0 2,2M2.5,4.5a1.3,1.3 0 1 0 1.5,2.5M12.5,3a1.3,1.3 0 1 0-2-2M11.5,3.5a1.3,1.3 0 1 0-1.5-2.5"/></svg><br>the lucky bone !</p></div>
    <div class="calorie-badge tiny">Less than 1 calories each</div>
  </section>

  <section class="label grape col-a" style="top:1000px">
    <div class="hearts-pattern" role="img" aria-label="White outline hearts pattern"></div>
    <div class="front-panel">
      <svg viewBox="0 0 124 164"><path d="M16,0H108L116,55Q125,62 124,82Q125,102 116,110L108,164H16L8,110Q-1,102 0,82Q-1,62 8,55Z"/></svg>
      <div class="kicker">Limited Ingredient</div>
      <div class="category">DOG TREATS</div>
      <div class="seal"><span class="seal-name">Goofy Pup</span></div>
      <div class="product-name">Ruby’s Snacks</div>
      <div class="net-weight">Net Wt 4 OZ (113g)</div>
    </div>
    <div class="claims short"><p>No<br>Soy, corn,<br>wheat, eggs<br>or dairy</p><p>Made with<br>vegan cheese</p></div>
    <div class="calorie-badge small">Only 1.5 calories each</div>
  </section>
  <section class="label grape col-b" style="top:1000px">
    <div class="hearts-pattern" role="img" aria-label="White outline hearts pattern"></div>
    <div class="front-panel">
      <svg viewBox="0 0 124 164"><path d="M16,0H108L116,55Q125,62 124,82Q125,102 116,110L108,164H16L8,110Q-1,102 0,82Q-1,62 8,55Z"/></svg>
      <div class="kicker">Limited Ingredient</div>
      <div class="category">DOG TREATS</div>
      <div class="seal"><span class="seal-name">Goofy Pup</span></div>
      <div class="product-name">Ruby’s Snacks</div>
      <div class="net-weight">Net Wt 4 OZ (113g)</div>
    </div>
    <div class="claims short"><p>No<br>Soy, corn,<br>wheat, eggs<br>or dairy</p><p>Made with<br>vegan cheese</p></div>
    <div class="calorie-badge small">Only 1.5 calories each</div>
  </section>

</div>
</body>
</html>
```